User Interface design for the Leaf Butler watering device

Hi Designers

I am designing a new pot plant watering device that clips onto the side of a pot plant and squirts water onto the plant when dry.
I need a designer to come up with an easy to use interface.

Objectives: Simple to understand interface for the average user. User should be able to understand the interface without having to read a manual. The 'feel' should be warm and friendly but also clean. The plan is to print this design on top of any buttons or lights which built into the device. (I can create/move/organise buttons and LED lights, so don't let that constrain the design)

The user interface should have the following options that the user can select:

A. Sensor selection:
1. Semi-wet soil
2. Semi-Dry Soil
3. Wet Soil.
4. Maintain current moisture level

B. Manual override:
1. Water for 5 seconds (small),
2. Water for 10 seconds (medium)
3. Water for 20 seconds (large)
AND
1. Watering frequency 1 day,
2. Watering Frequency 3 days.
3. Watering frequency 7 days.

C. Start/Stop button

Looking forward to your interpretations and designs!
ps: I've already had two logos designed which are provided below and should be incorporated.

Target Market(s)

Home user. Simple to use. Smart home device.

Requirements
Must have
• It should incorporate one of the previous logo designs.

```html
<!DOCTYPE html>
<html lang="en">
<head>
<meta charset="utf-8">
<title>Leaf Butler – Control Panel</title>
<link rel="stylesheet" href="https://fonts.googleapis.com/css2?family=Open+Sans:wght@400;600;700&family=Roboto+Condensed:wght@700&display=swap">
<style>
  :root{
    --blue:#1f5ea8;
    --blue-dark:#174a86;
    --green:#6cc52c;
    --green-ring:#9ad85a;
    --green-light:#d9f5a8;
    --tag-grey:#5b5b5b;
    --ink:#1c1c1c;
    --divider:#555555;
    --paper:#ffffff;
  }
  *{box-sizing:border-box;margin:0;padding:0}
  html,body{width:1200px;height:900px;overflow:hidden;background:var(--paper)}
  body{position:relative;font-family:"Open Sans",Arial,sans-serif;color:var(--blue)}
  .divider{position:absolute;left:617px;top:0;width:3px;height:900px;background:var(--divider)}
  .panel{position:absolute;top:0;width:620px;height:900px}
  .panel--off{left:0}
  .panel--on{left:562px}
  .panel > *{position:absolute}

  .state-tag{left:225px;top:0;width:240px;height:93px;display:flex;align-items:center;justify-content:center;color:#fff;font-size:30px;font-weight:400}
  .panel--off .state-tag{background:var(--tag-grey)}
  .panel--on .state-tag{background:var(--green)}

  .brand{left:327px;top:225px;transform:translate(-50%,-50%);display:flex;align-items:center;gap:12px;white-space:nowrap}
  .brand__name{font-size:50px;font-weight:700;color:var(--ink);letter-spacing:-1px}
  .brand__dot{width:22px;height:22px;border-radius:50%;background:var(--green)}

  .bracket{left:135px;width:413px;height:21px;border:2px solid var(--blue);border-bottom:none}
  .bracket--sensor{top:306px}
  .bracket--water{top:478px}
  .section-label{left:338px;transform:translateX(-50%);height:28px;padding:0 10px;background:var(--paper);border:2px solid var(--blue);border-radius:3px;font-size:20px;line-height:24px;white-space:nowrap}
  .section-label--sensor{top:291px}
  .section-label--water{top:464px}

  .mode{top:334px;width:110px;transform:translateX(-50%);display:flex;flex-direction:column;align-items:center}
  .mode svg{width:54px;height:54px}
  .mode__name{margin-top:10px;font-family:"Roboto Condensed",Arial,sans-serif;font-weight:700;font-size:13px;line-height:15px;text-align:center;text-transform:uppercase}
  .mode--semidry{left:132px}
  .mode--semiwet{left:272px}
  .mode--wet{left:420px}
  .mode--maintain{left:540px}

  .row-label{font-size:20px}
  .row-label--amount{left:108px;top:527px}
  .row-label--freq{left:102px;top:634px}

  .jug{top:518px;width:30px;height:40px}
  .jug--s{left:198px}.jug--m{left:339px}.jug--l{left:475px}

  .dose{top:517px;width:46px;height:46px;border-radius:50%;border:3px solid var(--green-ring);background:var(--paper);display:flex;align-items:center;justify-content:center;font-size:21px}
  .dose--s{left:234px}.dose--m{left:372px}.dose--l{left:513px}

  .interval{top:622px;width:57px;height:52px;border:3px solid var(--green-ring);border-radius:7px;background:var(--paper);display:flex;flex-direction:column;align-items:center;justify-content:center;line-height:1}
  .interval__num{font-size:22px}
  .interval__unit{font-size:11px;margin-top:3px}
  .interval--1{left:230px}.interval--3{left:370px}.interval--7{left:506px}

  .rule{left:97px;top:699px;width:481px;height:2px;background:var(--blue)}

  .power{left:303px;top:723px;width:57px;height:49px;border:3px solid var(--blue);border-radius:7px;background:var(--paper);display:flex;align-items:center;justify-content:center}
  .power svg{width:32px;height:32px}
  .power-label{left:393px;top:734px;font-size:20px}

  .is-lit{background:radial-gradient(circle at 50% 40%,var(--green-light) 0%,var(--green) 85%);border-color:var(--green-ring)}
  .power.is-lit{border-color:var(--blue)}
</style>
</head>
<body>

<svg width="0" height="0" style="position:absolute" aria-hidden="true">
  <defs>
    <symbol id="icon-half-sun" viewBox="0 0 48 48">
      <g stroke="#1f5ea8" stroke-width="2.5" stroke-linecap="round">
        <line x1="24" y1="3" x2="24" y2="10"/><line x1="24" y1="38" x2="24" y2="45"/>
        <line x1="3" y1="24" x2="10" y2="24"/><line x1="38" y1="24" x2="45" y2="24"/>
        <line x1="9" y1="9" x2="14" y2="14"/><line x1="34" y1="34" x2="39" y2="39"/>
        <line x1="9" y1="39" x2="14" y2="34"/><line x1="34" y1="14" x2="39" y2="9"/>
      </g>
      <circle cx="24" cy="24" r="10" fill="#fff" stroke="#1f5ea8" stroke-width="2.5"/>
      <path d="M24 14 A10 10 0 0 1 24 34 Z" fill="#1f5ea8"/>
    </symbol>
    <symbol id="icon-drop-outline" viewBox="0 0 48 48">
      <path d="M24 5 C24 5 12 22 12 31 A12 12 0 0 0 36 31 C36 22 24 5 24 5Z" fill="#fff" stroke="#1f5ea8" stroke-width="2.5"/>
      <path d="M24 12 C24 12 30 24 30 31 A6 6 0 0 1 24 38 Z" fill="#1f5ea8"/>
    </symbol>
    <symbol id="icon-drop-solid" viewBox="0 0 48 48">
      <path d="M24 5 C24 5 12 22 12 31 A12 12 0 0 0 36 31 C36 22 24 5 24 5Z" fill="#1f5ea8"/>
    </symbol>
    <symbol id="icon-maintain" viewBox="0 0 48 48">
      <path d="M33 8 A18 18 0 1 1 20 6.5" fill="none" stroke="#9ad85a" stroke-width="3"/>
      <path d="M30 2 L38 8 L30 13 Z" fill="#6cc52c"/>
      <path d="M24 14 C24 14 17 24 17 29 A7 7 0 0 0 31 29 C31 24 24 14 24 14Z" fill="#1f5ea8"/>
    </symbol>
    <symbol id="icon-jug" viewBox="0 0 30 40">
      <path d="M6 4 H26 V38 H6 Z M6 10 H2 V22 H6" fill="#fff" stroke="#1f5ea8" stroke-width="2"/>
    </symbol>
    <symbol id="icon-power" viewBox="0 0 32 32">
      <path d="M10 8 A11 11 0 1 0 22 8" fill="none" stroke="#1f5ea8" stroke-width="3" stroke-linecap="round"/>
      <line x1="16" y1="3" x2="16" y2="15" stroke="#1f5ea8" stroke-width="3" stroke-linecap="round"/>
    </symbol>
  </defs>
</svg>

<div class="divider"></div>

<!-- Panel: idle state -->
<section class="panel panel--off">
  <div class="state-tag">without light</div>
  <div class="brand"><span class="brand__name">Leaf Butler</span><span class="brand__dot"></span></div>

  <div class="bracket bracket--sensor"></div>
  <div class="section-label section-label--sensor">Soil Sensor</div>
  <div class="mode mode--semidry"><svg><use href="#icon-half-sun"/></svg><span class="mode__name">Semi-dry</span></div>
  <div class="mode mode--semiwet"><svg><use href="#icon-drop-outline"/></svg><span class="mode__name">Semi-wet</span></div>
  <div class="mode mode--wet"><svg><use href="#icon-drop-solid"/></svg><span class="mode__name">Wet</span></div>
  <div class="mode mode--maintain"><svg><use href="#icon-maintain"/></svg><span class="mode__name">Maintain<br>moisture</span></div>

  <div class="bracket bracket--water"></div>
  <div class="section-label section-label--water">Watering</div>

  <span class="row-label row-label--amount">Amount</span>
  <svg class="jug jug--s"><use href="#icon-jug"/><rect x="7" y="30" width="18" height="7" fill="#1f5ea8"/></svg>
  <div class="dose dose--s">5s</div>
  <svg class="jug jug--m"><use href="#icon-jug"/><rect x="7" y="22" width="18" height="15" fill="#1f5ea8"/></svg>
  <div class="dose dose--m">10s</div>
  <svg class="jug jug--l"><use href="#icon-jug"/><rect x="7" y="12" width="18" height="25" fill="#1f5ea8"/></svg>
  <div class="dose dose--l">20s</div>

  <span class="row-label row-label--freq">Frequency</span>
  <div class="interval interval--1"><span class="interval__num">1</span><span class="interval__unit">DAY</span></div>
  <div class="interval interval--3"><span class="interval__num">3</span><span class="interval__unit">DAYS</span></div>
  <div class="interval interval--7"><span class="interval__num">7</span><span class="interval__unit">DAYS</span></div>

  <div class="rule"></div>
  <div class="power"><svg><use href="#icon-power"/></svg></div>
  <span class="power-label">START/STOP</span>
</section>

<!-- Panel: lit state -->
<section class="panel panel--on">
  <div class="state-tag">within light</div>
  <div class="brand"><span class="brand__name">Leaf Butler</span><span class="brand__dot"></span></div>

  <div class="bracket bracket--sensor"></div>
  <div class="section-label section-label--sensor">Soil Sensor</div>
  <div class="mode mode--semidry"><svg><use href="#icon-half-sun"/></svg><span class="mode__name">Semi-dry</span></div>
  <div class="mode mode--semiwet"><svg viewBox="0 0 48 48"><circle cx="24" cy="24" r="22" fill="#6cc52c" stroke="#9ad85a" stroke-width="3"/><circle cx="24" cy="22" r="14" fill="#d9f5a8" opacity=".6"/><use href="#icon-drop-outline" x="10" y="9" width="28" height="28"/></svg><span class="mode__name">Semi-wet</span></div>
  <div class="mode mode--wet"><svg><use href="#icon-drop-solid"/></svg><span class="mode__name">Wet</span></div>
  <div class="mode mode--maintain"><svg><use href="#icon-maintain"/></svg><span class="mode__name">Maintain<br>moisture</span></div>

  <div class="bracket bracket--water"></div>
  <div class="section-label section-label--water">Watering</div>

  <span class="row-label row-label--amount">Amount</span>
  <svg class="jug jug--s"><use href="#icon-jug"/><rect x="7" y="30" width="18" height="7" fill="#1f5ea8"/></svg>
  <div class="dose dose--s is-lit">5s</div>
  <svg class="jug jug--m"><use href="#icon-jug"/><rect x="7" y="22" width="18" height="15" fill="#1f5ea8"/></svg>
  <div class="dose dose--m">10s</div>
  <svg class="jug jug--l"><use href="#icon-jug"/><rect x="7" y="12" width="18" height="25" fill="#1f5ea8"/></svg>
  <div class="dose dose--l">20s</div>

  <span class="row-label row-label--freq">Frequency</span>
  <div class="interval interval--1"><span class="interval__num">1</span><span class="interval__unit">DAY</span></div>
  <div class="interval interval--3 is-lit"><span class="interval__num">3</span><span class="interval__unit">DAYS</span></div>
  <div class="interval interval--7"><span class="interval__num">7</span><span class="interval__unit">DAYS</span></div>

  <div class="rule"></div>
  <div class="power is-lit"><svg><use href="#icon-power"/></svg></div>
  <span class="power-label">START/STOP</span>
</section>

</body>
</html>
```